Voyage Wellcare Hub Business Cards

We need business cards for our new start-up online travel health clinic. Visit our website voyagewellcarehub.ca for branding and more info.

Target Market(s)

Travellers

Industry/Entity Type

Business

Contact Information for Business Card

Maya Koslowski
maya@voyagewellcarehub.ca
+1 555 283 6194
voyagewellcarehub.ca

Font styles to use
Sans Serif

Colors
f68d4d

```html
<!DOCTYPE html>
<html lang="en">
<head>
<meta charset="utf-8">
<title>Voyage Wellcare Hub – Business Cards</title>
<link rel="stylesheet" href="https://fonts.googleapis.com/css2?family=Arimo:ital,wght@0,400;1,400&display=swap">
<style>
  :root {
    --orange: #f68d4d;
    --ink: #2a2327;
    --paper: #ffffff;
    --grey-text: #5a5a5a;
    --tag-grey: #8a8a8a;
    --rule: #b5b5b5;
    --stage: #d9d9d9;
  }
  * { box-sizing: border-box; margin: 0; padding: 0; }
  html, body { width: 1200px; height: 900px; overflow: hidden; }
  body {
    background: var(--stage);
    font-family: "Arimo", Arial, sans-serif;
    display: flex;
    flex-direction: column;
    align-items: center;
    justify-content: center;
    gap: 30px;
  }
  .card {
    position: relative;
    width: 720px;
    height: 411px;
    border-radius: 26px;
    overflow: hidden;
    box-shadow: 0 8px 24px rgba(0,0,0,0.18);
  }
  /* Back of card */
  .card--back { background: var(--ink); }
  .brand { position: absolute; text-align: right; }
  .brand__name {
    color: var(--orange);
    font-size: 46px;
    font-weight: 400;
    letter-spacing: 0.5px;
    white-space: nowrap;
  }
  .brand__tagline {
    color: var(--tag-grey);
    font-size: 16px;
    margin-top: 2px;
  }
  .card--back .brand {
    left: 50%; top: 50%;
    transform: translate(-50%, -50%);
  }
  .card--back .brand__tagline { color: #b9b9b9; }

  /* Front of card */
  .card--front { background: var(--paper); }
  .card--front .brand { right: 44px; top: 56px; }
  .rule-top {
    position: absolute; left: 300px; right: 44px; top: 150px;
    height: 1px; background: var(--rule);
  }
  .address {
    position: absolute; right: 44px; top: 186px;
    text-align: right; color: var(--grey-text);
    font-size: 17px; line-height: 1.35;
  }
  .person { position: absolute; left: 48px; top: 206px; right: 44px; }
  .person__head { display: flex; align-items: flex-end; gap: 14px; }
  .person__name { color: var(--orange); font-size: 25px; white-space: nowrap; }
  .person__rule { flex: 1; height: 1px; background: var(--rule); margin-bottom: 4px; }
  .person__role { color: var(--grey-text); font-style: italic; font-size: 18px; margin-top: 2px; }
  .contact { list-style: none; margin-top: 10px; }
  .contact li {
    display: flex; align-items: center; gap: 10px;
    color: var(--grey-text); font-size: 18px; line-height: 1.3;
  }
  .contact svg { width: 16px; height: 16px; flex: none; }
  .band {
    position: absolute; left: 0; right: 0; bottom: 0; height: 90px;
    background: var(--ink);
  }
  .band__web {
    position: absolute; left: 48px; bottom: 30px;
    color: var(--orange); font-size: 20px; letter-spacing: 0.3px;
  }
  .social { position: absolute; right: 44px; top: 18px; display: flex; gap: 12px; }
  .social span { width: 28px; height: 28px; border-radius: 50%; background: var(--paper); }
</style>
</head>
<body>
  <section class="card card--back">
    <div class="brand">
      <div class="brand__name">Voyage Wellcare Hub</div>
      <div class="brand__tagline">Online Travel Health Experts</div>
    </div>
  </section>

  <section class="card card--front">
    <div class="brand">
      <div class="brand__name">Voyage Wellcare Hub</div>
      <div class="brand__tagline">Online Travel Health Experts</div>
    </div>
    <div class="rule-top"></div>
    <div class="address">117 Harbour Ln, Kingston<br>ON K7L 2P4, Canada</div>
    <div class="person">
      <div class="person__head">
        <span class="person__name">Maya Koslowski</span>
        <span class="person__rule"></span>
      </div>
      <div class="person__role">travel expert</div>
      <ul class="contact">
        <li>
          <svg viewBox="0 0 16 16" aria-hidden="true"><circle cx="8" cy="8" r="7" fill="none" stroke="#f68d4d" stroke-width="1.4"/><path d="M5 6.5q3-2 6 0v1.5h-1.5l-.5-1h-2l-.5 1H5z" fill="#f68d4d"/><rect x="5.5" y="9" width="5" height="2" rx=".5" fill="#f68d4d"/></svg>
          +1 555 283 6194
        </li>
        <li>
          <svg viewBox="0 0 16 16" aria-hidden="true"><circle cx="8" cy="8" r="7" fill="none" stroke="#f68d4d" stroke-width="1.4"/><rect x="4.5" y="5.5" width="7" height="5" fill="#f68d4d"/><path d="M4.5 5.5l3.5 3 3.5-3" fill="none" stroke="#fff" stroke-width=".9"/></svg>
          maya@voyagewellcarehub.ca
        </li>
      </ul>
    </div>
    <div class="band">
      <div class="social" aria-label="Social media">
        <span></span><span></span><span></span>
      </div>
      <div class="band__web">voyagewellcarehub.ca</div>
    </div>
  </section>
</body>
</html>
```